Business Card Design for LeafCrest (Farming Devices)

We need Business Cards for our new Company based in Switzerland called "LeafCrest" We develop innovativ products for indoor and outdoor Farming for household and components for vertical farming. Our initial BloomNest gives people the possibility to grow their own food at home all year round. The design should communicate freshness, innovation, health.

```html
<!DOCTYPE html>
<html lang="en">
<head>
<meta charset="UTF-8">
<title>LeafCrest Business Card</title>
<link href="https://fonts.googleapis.com/css2?family=Lato:wght@700&family=Montserrat:wght@500;700&display=swap" rel="stylesheet">
<style>
  :root {
    --backdrop: #9a9a9a;
    --paper: #ffffff;
    --leaf-green: #76b543;
    --sky-blue: #006db8;
    --ink-light: #ffffff;
  }
  * { margin: 0; padding: 0; box-sizing: border-box; }
  html, body {
    width: 1133px;
    height: 1200px;
    overflow: hidden;
    background: var(--backdrop);
  }
  .canvas {
    position: relative;
    width: 1133px;
    height: 1200px;
  }
  .card {
    position: absolute;
    width: 722px;
    height: 411px;
    overflow: hidden;
  }
  .card--front { left: 197px; top: 144px; background: var(--paper); }
  .card--back  { left: 200px; top: 641px; background: var(--sky-blue); }

  .wordmark {
    position: absolute;
    left: 0;
    width: 100%;
    text-align: center;
    font-family: "Lato", sans-serif;
    font-weight: 700;
    font-size: 66px;
    letter-spacing: -0.5px;
    line-height: 1;
  }
  .card--front .wordmark { top: 82px; color: var(--sky-blue); }
  .card--back .wordmark  { top: 226px; color: var(--ink-light); }

  .swoosh {
    position: absolute;
    left: 0; top: 0;
    width: 722px;
    height: 411px;
  }

  .holder {
    position: absolute;
    right: 373px;
    top: 296px;
    text-align: right;
    font-family: "Montserrat", sans-serif;
    color: var(--ink-light);
    font-weight: 500;
    font-size: 15px;
    line-height: 20.5px;
  }
  .holder__name {
    font-weight: 700;
    font-size: 21px;
    line-height: 24px;
    margin-bottom: 1px;
  }

  .contact-list {
    position: absolute;
    left: 381px;
    top: 296px;
    list-style: none;
    font-family: "Montserrat", sans-serif;
    font-weight: 500;
    font-size: 15.5px;
    color: var(--ink-light);
  }
  .contact-list li {
    display: flex;
    align-items: center;
    height: 20.7px;
  }
  .contact-list svg {
    width: 13px;
    height: 13px;
    margin-right: 10px;
    flex: none;
  }
</style>
</head>
<body>
<div class="canvas">

  <section class="card card--front" aria-label="Business card front">
    <svg class="swoosh" viewBox="0 0 722 411" aria-hidden="true">
      <path d="M0 316 Q 340 88 722 322 L722 411 L0 411 Z" fill="var(--sky-blue)"/>
      <path d="M0 362 Q 350 108 722 326" fill="none" stroke="var(--paper)" stroke-width="5"/>
      <path d="M0 362 Q 350 108 722 326 L722 411 L0 411 Z" fill="var(--leaf-green)"/>
    </svg>

    <h1 class="wordmark">LeafCrest</h1>

    <div class="holder">
      <p class="holder__name">Daniel Moore</p>
      <p>President</p>
      <p>4120 Meadow Way</p>
      <p>Lucerne, Switzerland 6003</p>
    </div>

    <ul class="contact-list">
      <li>
        <svg viewBox="0 0 16 16" aria-hidden="true"><path fill="#fff" d="M3.5 1 L6 1 L7 4.5 L5.3 6 Q6.5 9 10 10.7 L11.5 9 L15 10 L15 12.5 Q14 15 11.5 15 Q1 13 1 3.5 Q1 1.5 3.5 1 Z"/></svg>
        041-555-2870
      </li>
      <li>
        <svg viewBox="0 0 16 16" aria-hidden="true"><rect x="4" y="1" width="8" height="14" rx="1.5" fill="none" stroke="#fff" stroke-width="1.8"/><circle cx="8" cy="12.3" r="0.9" fill="#fff"/></svg>
        079-555-6142
      </li>
      <li>
        <svg viewBox="0 0 16 16" aria-hidden="true"><rect x="1.5" y="4" width="13" height="9" fill="#fff"/><path d="M1.5 4 L8 9 L14.5 4" fill="none" stroke="var(--leaf-green)" stroke-width="1.2"/></svg>
        moore@leafcrest.com
      </li>
      <li>
        <svg viewBox="0 0 16 16" aria-hidden="true"><circle cx="8" cy="8" r="6.5" fill="#fff"/><path d="M4 5 Q6 6 6 8 Q8 9 7 12 M10 3.5 Q9 6 11 7 Q13 7 13.5 9" fill="none" stroke="var(--leaf-green)" stroke-width="1.3"/></svg>
        www.leafcrest.com
      </li>
    </ul>
  </section>

  <section class="card card--back" aria-label="Business card back">
    <h2 class="wordmark">LeafCrest</h2>
  </section>

</div>
</body>
</html>
```